OLUM Sign
OLUM leasing sign
#12 I'd like to go with this design with a few minor changes. Could you please change the font of Daniel Pruett to something that works better with the other font Office space? and can you remove the rectangles under the phone number? I promise i'll respond more quickly once i see the revisions.
additional comment on 23 -24. I think I like these for their clean simplicity (although they need the required information and the proper logo)
#23 ,#24 These looks different - good. Can you try a grey background, with correct logo (maybe in white). There is now an .eps file available. The sign must have phone number, "Office Space", and Realtor's name. use only the colors in logo, and black.
Dear PH, thanks for your valuable feedback.Will submit some more design options...regards,
will upload vector file. these designs are not what we are looking for. we want an eye catching creative design that doesn't look like a typical leasing sign.
Dear PH, Can you please upload the vector file (.ai or .eps) of the logo.Regards.

```html
<!DOCTYPE html>
<html lang="en">
<head>
<meta charset="utf-8">
<title>OLUM Leasing Sign – Office Space Available</title>
<link rel="stylesheet" href="https://fonts.googleapis.com/css2?family=Archivo+Black&family=Alfa+Slab+One&family=Montserrat:wght@800&family=Bitter:wght@400;700&display=swap">
<style>
  :root {
    --cream-light: #fffdf2;
    --cream: #fbf3c8;
    --cream-soft: #f7ecc0;
    --banner-yellow: #ffe85a;
    --banner-yellow-deep: #f5c400;
    --corner-red: #c8101c;
    --corner-red-deep: #8e0710;
    --headline-red: #c3121d;
    --headline-red-dark: #8a0a12;
    --ink: #1c1c1c;
    --ink-grey: #3a3a3a;
    --accent-orange: #c8561a;
    --logo-grey: #6f6f6f;
    --frame-grey: #c9c4a8;
    --chair-yellow: #f6c21b;
    --chair-yellow-light: #ffe071;
  }

  html, body {
    margin: 0;
    padding: 0;
    overflow: hidden;
    background: #ffffff;
  }

  .sign {
    position: relative;
    width: 1200px;
    height: 799px;
    overflow: hidden;
    background: radial-gradient(ellipse at 60% 40%, var(--cream-light) 0%, var(--cream) 100%);
  }

  .sign__backdrop {
    position: absolute;
    left: 0;
    top: 520px;
    width: 1200px;
    height: 279px;
    background: linear-gradient(180deg, rgba(255, 255, 255, 0) 0%, rgba(255, 255, 255, 0.55) 45%, var(--cream-soft) 100%);
  }

  /* Top banner */
  .banner {
    position: absolute;
    left: 0;
    top: 0;
    width: 1200px;
    height: 118px;
  }

  .banner__label {
    position: absolute;
    left: 0;
    top: 4px;
    width: 1200px;
    text-align: center;
    font-family: "Archivo Black", sans-serif;
    font-size: 106px;
    line-height: 104px;
    letter-spacing: 6px;
    color: var(--ink-grey);
    margin: 0;
  }

  /* Illustration area */
  .chair-art {
    position: absolute;
    left: 18px;
    top: 190px;
    width: 180px;
    height: 310px;
    border-radius: 40px 40px 20px 20px;
    background: linear-gradient(160deg, var(--chair-yellow-light) 0%, var(--chair-yellow) 70%, #b8b8b8 100%);
  }

  /* Headline band */
  .headline {
    position: absolute;
    left: 212px;
    top: 206px;
    width: 988px;
    height: 124px;
  }

  .headline__tab {
    position: absolute;
    left: 0;
    top: 0;
    width: 28px;
    height: 124px;
    border-radius: 12px 0 0 12px;
    background: linear-gradient(180deg, var(--corner-red) 0%, var(--corner-red-deep) 100%);
  }

  .headline__strip {
    position: absolute;
    left: 28px;
    top: 0;
    right: 0;
    height: 124px;
    background: linear-gradient(180deg, #ffffff 0%, #f4f0dc 100%);
  }

  .headline__text {
    position: absolute;
    left: 40px;
    top: 0;
    margin: 0;
    font-family: "Alfa Slab One", serif;
    font-size: 112px;
    line-height: 124px;
    letter-spacing: 1px;
    color: var(--headline-red);
    background: linear-gradient(180deg, #e23a32 0%, var(--headline-red) 50%, var(--headline-red-dark) 100%);
    -webkit-background-clip: text;
    background-clip: text;
    -webkit-text-fill-color: transparent;
    white-space: nowrap;
  }

  /* Phone line */
  .phone {
    position: absolute;
    left: 304px;
    top: 364px;
    display: flex;
    align-items: center;
    gap: 54px;
  }

  .phone__icon {
    width: 110px;
    height: 110px;
  }

  .phone__number {
    font-family: "Montserrat", sans-serif;
    font-weight: 800;
    font-size: 102px;
    line-height: 110px;
    color: var(--ink);
    margin: 0;
    white-space: nowrap;
  }

  /* Brand box */
  .brand {
    position: absolute;
    left: 36px;
    top: 600px;
    width: 456px;
    height: 166px;
    box-sizing: border-box;
    border: 3px solid var(--frame-grey);
    border-radius: 22px;
    background: linear-gradient(180deg, #ffffff 0%, #f3efdd 100%);
    display: flex;
    align-items: center;
    justify-content: center;
  }

  .brand__name {
    font-family: "Archivo Black", sans-serif;
    font-size: 112px;
    line-height: 1;
    letter-spacing: 6px;
    color: var(--logo-grey);
  }

  /* Contact */
  .contact {
    position: absolute;
    left: 520px;
    top: 600px;
    width: 636px;
  }

  .contact__role {
    margin: 0;
    text-align: right;
    font-family: "Bitter", serif;
    font-weight: 400;
    font-size: 56px;
    line-height: 72px;
    color: var(--ink);
  }

  .contact__rule {
    height: 4px;
    margin: 8px 0 4px 0;
    background: linear-gradient(90deg, rgba(200, 86, 26, 0) 0%, var(--accent-orange) 25%, var(--accent-orange) 100%);
  }

  .contact__name {
    margin: 0;
    text-align: right;
    font-family: "Bitter", serif;
    font-weight: 700;
    font-size: 78px;
    line-height: 80px;
    font-variant: small-caps;
    letter-spacing: 2px;
    color: var(--accent-orange);
    white-space: nowrap;
  }
</style>
</head>
<body>
<main class="sign">

  <div class="sign__backdrop" aria-hidden="true"></div>

  <header class="banner">
    <svg width="1200" height="118" viewBox="0 0 1200 118" aria-hidden="true">
      <defs>
        <linearGradient id="bannerFill" x1="0" y1="0" x2="0" y2="1">
          <stop offset="0" stop-color="#fff7a8"/>
          <stop offset="0.5" stop-color="#ffe85a"/>
          <stop offset="1" stop-color="#f5c400"/>
        </linearGradient>
        <linearGradient id="cornerFill" x1="0" y1="0" x2="0" y2="1">
          <stop offset="0" stop-color="#e8323a"/>
          <stop offset="1" stop-color="#8e0710"/>
        </linearGradient>
      </defs>
      <rect x="24" y="2" width="1152" height="108" rx="12" fill="url(#bannerFill)"/>
      <path d="M24 2 H150 L24 96 Z" fill="url(#cornerFill)"/>
      <path d="M1176 110 H1050 L1176 16 Z" fill="url(#cornerFill)"/>
      <circle cx="60" cy="28" r="10" fill="#e6e6e6" stroke="#777" stroke-width="2"/>
      <line x1="53" y1="28" x2="67" y2="28" stroke="#555" stroke-width="2"/>
      <circle cx="1140" cy="84" r="10" fill="#e6e6e6" stroke="#777" stroke-width="2"/>
      <line x1="1133" y1="84" x2="1147" y2="84" stroke="#555" stroke-width="2"/>
    </svg>
    <h1 class="banner__label">AVAILABLE</h1>
  </header>

  <div class="chair-art" role="img" aria-label="Yellow office chair illustration"></div>

  <section class="headline">
    <div class="headline__tab"></div>
    <div class="headline__strip"></div>
    <h2 class="headline__text">OFFICE SPACE</h2>
  </section>

  <div class="phone">
    <svg class="phone__icon" viewBox="0 0 96 96" role="img" aria-label="Telephone">
      <path d="M10 30 C 10 14, 86 14, 86 30 L 86 38 L 66 38 L 64 28 L 32 28 L 30 38 L 10 38 Z" fill="#c3121d"/>
      <path d="M22 42 L 74 42 L 86 84 L 10 84 Z" fill="#c3121d"/>
      <circle cx="48" cy="62" r="14" fill="#ffffff"/>
      <circle cx="48" cy="62" r="5" fill="#c3121d"/>
    </svg>
    <p class="phone__number">215-555-0147</p>
  </div>

  <div class="brand">
    <span class="brand__name">OLUM</span>
  </div>

  <section class="contact">
    <p class="contact__role">Contact Person</p>
    <div class="contact__rule"></div>
    <p class="contact__name">Daniel Pruett</p>
  </section>

</main>
</body>
</html>
```